Redesign of SnapHarbor Lumora Mobile app

The App exists, is up and running but the design is not the best (my creation and i am a developer).
Project landing page http://snapharbor.example/

Also the app has live tiles small, medium and large.

The purpose of this is to have a professional design and make this app the best app on the Lumora Mobile marketplace of his kind.

This app is a picture library that tells you where you've made you're pictures and gives you a unique perspective on the places that you have visited.

If this is successful there will be a version for Lumora 8, Zentrix and QOS also.

The app right now is for LM7 and LM8 and because of this the performance is not the best. With this new design the app will be for LM8 only and have the best performance possible.

I am not sure what else should i mention here but i am glad to answer to any questions if you are interested.

I am using Vantor draft as a design tool and Vantor Mixer and Crafton bench as development tools so if you can provide compatible file the better but is not mandatory.

It wold be nice to keep the existing color palette but again nothing is mandatory I just need a good design.

Links:
App on Marketplace http://www.appdepotmobile.example/en-us/store/app/snapharbor/7a3f9d21-0b6c-4e8d-9f12-ab34cd56ef78

App landing page http://snapharbor.example/
Updates

Reason: The submission time was extended doe to the request of designers.

We can do better, I will increase the budget with 200$  so the total budget will be 480$ so please consider this more seriously.

Thank you.

Target Market(s)

Lumora Mobile users that travel and make pictures.

Industry/Entity Type

Library

Requirements
Must have
• Panorama control as the App main page like in the present.

Representation of visited locations , Live tiles, Map, share location and picture..

If the designer comes up with better proposition they will be take in consideration.

None of these are mandatory but we should keep a connection with the present design so the users will not have the impression that this is a totally different app, this is SnapHarbor but better, more professional.

```html
<!DOCTYPE html>
<html lang="en">
<head>
<meta charset="utf-8">
<title>SnapHarbor – app screens</title>
<link rel="stylesheet" href="https://fonts.googleapis.com/css2?family=Open+Sans:wght@300;400;600&display=swap">
<style>
  :root {
    --stage: #f3971f;
    --screen: #ecebe8;
    --appbar: #1f1f1f;
    --accent: #2b9cd8;
    --brand-pin: #f39221;
    --ink: #3a3a3a;
    --ink-soft: #6a6a6a;
    --field: #e0e0e0;
    --field-line: #c9c9c9;
    --white: #ffffff;
  }
  * { box-sizing: border-box; margin: 0; padding: 0; }
  html, body { width: 1200px; height: 1000px; overflow: hidden; }
  body {
    position: relative;
    background: var(--stage);
    font-family: "Open Sans", "Segoe UI", sans-serif;
    color: var(--ink);
  }
  .screen {
    position: absolute;
    top: 215px;
    width: 271px;
    height: 480px;
    background: var(--screen);
    overflow: hidden;
  }
  .screen--library { left: 67px; }
  .screen--share-chirp { left: 457px; }
  .screen--share-circle { left: 857px; }

  /* Library screen */
  .album-title { position: absolute; left: 13px; top: 44px; font-weight: 300; font-size: 22px; }
  .album-title small { font-size: 11px; color: var(--ink-soft); margin-left: 3px; }
  .photo-grid {
    position: absolute; left: 13px; top: 76px;
    display: grid; grid-template-columns: repeat(4, 56px); gap: 7px;
  }
  .thumb {
    position: relative; width: 56px; height: 56px;
    border: 2px solid var(--accent);
    background: linear-gradient(180deg, #8a8f93 0%, #b7a9a4 45%, #5b524e 70%, #3d3a38 100%);
  }
  .thumb--checked::after {
    content: ""; position: absolute; right: -2px; top: -2px;
    border-top: 16px solid var(--accent); border-left: 16px solid transparent;
  }
  .thumb--checked svg { position: absolute; right: 0; top: 0; z-index: 1; }

  .appbar {
    position: absolute; left: 0; right: 0; bottom: 0;
    background: var(--appbar); color: var(--white);
  }
  .appbar--library { height: 56px; }
  .appbar--share { height: 38px; }
  .appbar .more { position: absolute; right: 10px; top: 0; font-size: 14px; letter-spacing: 1px; line-height: 12px; }
  .appbar-action { position: absolute; top: 8px; width: 50px; text-align: center; font-size: 7px; }
  .appbar-action svg { display: block; margin: 0 auto 3px; }

  /* Share screens */
  .brand { position: absolute; left: 10px; top: 22px; display: flex; align-items: center; gap: 5px; }
  .brand-name { font-weight: 300; font-size: 21px; color: var(--accent); }
  .brand-dot { width: 10px; height: 10px; border-radius: 50%; background: var(--brand-pin); }
  .network { position: absolute; right: 12px; top: 27px; font-size: 11px; font-weight: 600; color: var(--accent); }
  .avatar {
    position: absolute; left: 10px; width: 56px; height: 56px; border-radius: 50%;
    border: 2px solid var(--accent);
    background: radial-gradient(circle at 50% 40%, #d9d9d9 0%, #8f8f8f 60%, #3c3c3c 100%);
  }
  .profile-name { position: absolute; left: 71px; font-weight: 300; font-size: 22px; line-height: 1; }
  .profile-count { position: absolute; left: 71px; font-weight: 300; font-size: 19px; line-height: 1; }
  .profile-count small { font-size: 15px; }
  .post-photo {
    position: absolute; left: 9px; width: 251px; height: 143px;
    border: 2px solid var(--accent); border-bottom: none;
    background: radial-gradient(ellipse at 45% 70%, #c9c39a 0%, #7d6a48 35%, #3e2f20 75%, #221810 100%);
  }
  .place-bar {
    position: absolute; left: 9px; width: 251px; height: 22px;
    background: var(--accent); color: var(--white);
    text-align: right; padding-right: 6px; font-size: 15px; line-height: 22px;
  }
  .place-bar small { font-size: 11px; }
  .message-label { position: absolute; left: 9px; font-size: 16px; }
  .message-meta { position: absolute; right: 10px; font-size: 8px; color: var(--ink-soft); display: flex; align-items: center; gap: 4px; }
  .checkbox { width: 11px; height: 11px; border: 1px solid var(--ink); display: inline-flex; align-items: center; justify-content: center; }
  .message-field {
    position: absolute; left: 9px; width: 251px; height: 92px;
    background: var(--field); border: 1px solid var(--field-line);
    padding: 4px 6px; font-size: 11px; color: var(--ink-soft);
  }
</style>
</head>
<body>

<!-- Library screen -->
<section class="screen screen--library">
  <h1 class="album-title">Paris <small>178 pictures</small></h1>
  <div class="photo-grid" role="img" aria-label="Grid of Paris street photos">
    <div class="thumb"></div><div class="thumb"></div><div class="thumb"></div><div class="thumb"></div>
    <div class="thumb"></div><div class="thumb"></div><div class="thumb"></div><div class="thumb"></div>
    <div class="thumb"></div><div class="thumb"></div>
    <div class="thumb thumb--checked"><svg width="10" height="10" viewBox="0 0 10 10"><path d="M1.5 5 L4 7.5 L8.5 2" fill="none" stroke="#fff" stroke-width="1.5"/></svg></div>
    <div class="thumb"></div>
    <div class="thumb"></div><div class="thumb"></div><div class="thumb"></div><div class="thumb"></div>
    <div class="thumb"></div><div class="thumb"></div><div class="thumb"></div><div class="thumb"></div>
    <div class="thumb"></div><div class="thumb"></div><div class="thumb"></div><div class="thumb"></div>
  </div>
  <nav class="appbar appbar--library">
    <div class="appbar-action" style="left:62px">
      <svg width="26" height="26" viewBox="0 0 26 26"><circle cx="13" cy="13" r="12" fill="none" stroke="#fff" stroke-width="1.6"/><path d="M7.5 13.5 L11.5 17 L18.5 9" fill="none" stroke="#fff" stroke-width="2"/></svg>uncheck
    </div>
    <div class="appbar-action" style="left:110px">
      <svg width="26" height="26" viewBox="0 0 26 26"><circle cx="13" cy="13" r="12" fill="none" stroke="#fff" stroke-width="1.6"/><path d="M9 9 L17 17 M17 9 L9 17" stroke="#fff" stroke-width="2"/></svg>clear
    </div>
    <div class="appbar-action" style="left:158px">
      <svg width="26" height="26" viewBox="0 0 26 26"><circle cx="13" cy="13" r="12" fill="none" stroke="#fff" stroke-width="1.6"/><path d="M13 20 C9 15 8.5 13 8.5 11.5 A4.5 4.5 0 0 1 17.5 11.5 C17.5 13 17 15 13 20 Z" fill="none" stroke="#fff" stroke-width="1.6"/><circle cx="13" cy="11.5" r="1.6" fill="#fff"/></svg>add to map
    </div>
    <span class="more">...</span>
  </nav>
</section>

<!-- Share screen: Chirpwave -->
<section class="screen screen--share-chirp">
  <div class="brand"><span class="brand-name">SnapHarbor</span><span class="brand-dot"></span></div>
  <span class="network">Chirpwave</span>
  <div class="avatar" style="top:70px" role="img" aria-label="Profile portrait"></div>
  <p class="profile-name" style="top:73px">@genhensley</p>
  <p class="profile-count" style="top:102px">127 <small>followers</small></p>
  <div class="post-photo" style="top:142px" role="img" aria-label="Photo of skulls and bones in the Paris catacombs"></div>
  <div class="place-bar" style="top:285px">Paris, France <small>Catacombes de Paris</small></div>
  <p class="message-label" style="top:314px">Message</p>
  <p class="message-meta" style="top:322px">124 characters remaining</p>
  <div class="message-field" style="top:339px">This is amazing!</div>
  <nav class="appbar appbar--share">
    <div class="appbar-action" style="left:85px;top:6px">
      <svg width="26" height="26" viewBox="0 0 26 26"><circle cx="13" cy="13" r="12" fill="none" stroke="#fff" stroke-width="1.6"/><path d="M7.5 8.5 H18.5 V15.5 H11 L8.5 18 V15.5 H7.5 Z" fill="#fff"/></svg>
    </div>
    <div class="appbar-action" style="left:133px;top:6px">
      <svg width="26" height="26" viewBox="0 0 26 26"><circle cx="13" cy="13" r="12" fill="none" stroke="#fff" stroke-width="1.6"/><path d="M8.5 8.5 H17.5 M11 8.5 V7 H15 V8.5 M9.5 10 L10.3 19 H15.7 L16.5 10 Z M12 11.5 V17.5 M14 11.5 V17.5" fill="none" stroke="#fff" stroke-width="1.3"/></svg>
    </div>
    <span class="more">...</span>
  </nav>
</section>

<!-- Share screen: Circlebook -->
<section class="screen screen--share-circle">
  <div class="brand"><span class="brand-name">SnapHarbor</span><span class="brand-dot"></span></div>
  <span class="network">Circlebook</span>
  <div class="avatar" style="top:68px" role="img" aria-label="Profile portrait"></div>
  <p class="profile-name" style="top:72px">Walter Hensley</p>
  <p class="profile-count" style="top:100px">77 <small>friends</small></p>
  <div class="post-photo" style="top:140px" role="img" aria-label="Photo of skulls and bones in the Paris catacombs"></div>
  <div class="place-bar" style="top:283px">Paris, France <small>Catacombes de Paris</small></div>
  <p class="message-label" style="top:312px">Message</p>
  <p class="message-meta" style="top:317px">
    <span class="checkbox"><svg width="9" height="9" viewBox="0 0 10 10"><path d="M1.5 5 L4 7.5 L8.5 2" fill="none" stroke="#3a3a3a" stroke-width="1.5"/></svg></span>Hide location
  </p>
  <div class="message-field" style="top:336px">This is amazing!</div>
  <nav class="appbar appbar--share">
    <div class="appbar-action" style="left:85px;top:6px">
      <svg width="26" height="26" viewBox="0 0 26 26"><circle cx="13" cy="13" r="12" fill="none" stroke="#fff" stroke-width="1.6"/><path d="M7.5 8.5 H18.5 V15.5 H11 L8.5 18 V15.5 H7.5 Z" fill="#fff"/></svg>
    </div>
    <div class="appbar-action" style="left:133px;top:6px">
      <svg width="26" height="26" viewBox="0 0 26 26"><circle cx="13" cy="13" r="12" fill="none" stroke="#fff" stroke-width="1.6"/><path d="M8.5 8.5 H17.5 M11 8.5 V7 H15 V8.5 M9.5 10 L10.3 19 H15.7 L16.5 10 Z M12 11.5 V17.5 M14 11.5 V17.5" fill="none" stroke="#fff" stroke-width="1.3"/></svg>
    </div>
    <span class="more">...</span>
  </nav>
</section>

</body>
</html>
```